Front and content page design for Fitness Cookbook

I am looking for someone to Design a front cover for a Recipe book and also create an amazing layout for the book.

Its for a corporate seminar so has to be eye catching, professional and bold.

Content is complete

Target Market(s)

Industry/Entity Type

Health And Wellness

Font styles to use
Sans Serif

Requirements
Must have
• Eye catching, professional and bold.
• By Dorian as stated on the document
• Must have Velmora Athletics Logo on it.

```html
<!DOCTYPE html>
<html lang="en">
<head>
<meta charset="utf-8">
<title>Homemade Beef Burgers</title>
<link href="https://fonts.googleapis.com/css2?family=Oswald:wght@400&family=Arimo:wght@400;700&display=swap" rel="stylesheet">
<style>
  :root {
    --orange: #e8731e;
    --orange-soft: #f3a050;
    --ink: #2a2a2a;
    --panel: #fbeee0;
    --panel-shadow: #d9d2c8;
    --page: #ffffff;
    --photo-dark: #3b3a2f;
    --photo-mid: #8a6a52;
  }
  * { margin: 0; padding: 0; box-sizing: border-box; }
  html, body {
    width: 849px; height: 1200px; overflow: hidden; background: var(--page);
  }
  .recipe-page {
    position: relative; width: 849px; height: 1200px;
    font-family: "Arimo", Arial, sans-serif; color: var(--ink);
  }
  .recipe-title {
    position: absolute; left: 106px; top: 100px;
    font-family: "Oswald", "Arial Narrow", sans-serif; font-weight: 400;
    font-size: 82px; line-height: 1; color: var(--orange); letter-spacing: -0.5px;
  }
  .title-rule {
    position: absolute; left: 106px; top: 230px; width: 648px; height: 2px;
    background: var(--orange);
  }
  .ingredients-panel {
    position: absolute; left: 108px; top: 250px; width: 318px; height: 340px;
    background: var(--panel); padding: 24px 22px;
    box-shadow: 8px 8px 10px var(--panel-shadow);
    font-size: 15px; line-height: 1.22;
  }
  .recipe-times { margin-bottom: 14px; }
  .section-heading { font-weight: 700; font-style: italic; margin-bottom: 2px; }
  .ingredient-list { list-style: none; }
  .instructions {
    position: absolute; left: 452px; top: 318px; width: 300px;
    font-size: 15px; line-height: 1.25;
  }
  .instructions .section-heading { margin-bottom: 12px; }
  .photo-frame {
    position: absolute; left: 108px; top: 606px; width: 652px; height: 500px;
    background: linear-gradient(135deg, var(--orange-soft), var(--orange));
    padding: 14px;
  }
  .dish-photo {
    width: 100%; height: 100%; border: 10px solid var(--page);
    background: radial-gradient(ellipse at 50% 50%, var(--photo-mid) 0%, #6e5a44 40%, var(--photo-dark) 100%);
  }
</style>
</head>
<body>
<main class="recipe-page">
  <h1 class="recipe-title">Homemade Beef Burgers</h1>
  <div class="title-rule"></div>

  <section class="ingredients-panel">
    <p class="recipe-times">Prep time: 5 mins<br>Cooking time: 20 mins</p>
    <h2 class="section-heading">Ingredients:</h2>
    <ul class="ingredient-list">
      <li>Makes 3-4 burgers</li>
      <li>500g grass fed lean beef mince</li>
      <li>1 whole egg</li>
      <li>1 egg white</li>
      <li>1tsp coconut oil</li>
      <li>½ cup onions</li>
      <li>2 cloves garlic</li>
      <li>2 fresh chillies (optional)</li>
      <li>Salt, pepper, mixed herbs to taste</li>
      <li>2 handful of spinach</li>
      <li>4 slices of beetroot</li>
    </ul>
  </section>

  <section class="instructions">
    <h2 class="section-heading">Cooking Instructions:</h2>
    <p>Mash the egg and egg white into the mince and add the onions, garlic, chillies and spices in the same bowl. Use your hands to mould the mixture into 3-4 patties. Fry the patties in the coconut oil on a medium heat, turning throughout till cooked. Layer the spinach and beetroot on top of each one.</p>
  </section>

  <div class="photo-frame">
    <div class="dish-photo" role="img" aria-label="Photo of two beef burger patties topped with spinach leaves and beetroot slices on a plate"></div>
  </div>
</main>
</body>
</html>
```